New Company Business Card Design

I have a new company logo and I want a new business card design. I dont know if the logo file i attached is in the correct format or quality. We are a New York City Specialty construction Firm specializing in high risk out of the box projects. I want a simple and classy business card that people will his card is as crisp as the work his company does.

Target Market(s)

Clients in the heavy construction industry in New York City

Industry/Entity Type

Construction Company

Contact Information for Business Card

Simple Classy - DIFFERENT

Font styles to use
Other font styles liked:
• Mach the logo font in some way

Colors

Designer to choose colors to be used in the design.

Requirements
Must have
• Uniqueness
Nice to have
• Nothing particular - Just different and classy - Timeless
Should not have
• Goofy Shit or Gimmicky shit

```html
<!DOCTYPE html>
<html lang="en">
<head>
<meta charset="utf-8">
<title>Halden Works, Inc. — Business Card</title>
<link href="https://fonts.googleapis.com/css2?family=Lato:wght@400;700;900&display=swap" rel="stylesheet">
<style>
  :root {
    --bg: #d9d9d9;
    --card: #ffffff;
    --brand-blue: #1a67b0;
    --navy: #1f3f7a;
    --band-text: #ffffff;
    --shadow: rgba(0,0,0,0.18);
  }
  * { box-sizing: border-box; margin: 0; padding: 0; }
  html, body { width: 1200px; height: 1200px; overflow: hidden; }
  body {
    background: var(--bg);
    font-family: "Lato", Arial, sans-serif;
    display: flex;
    flex-direction: column;
    align-items: center;
    justify-content: space-evenly;
  }
  .card {
    position: relative;
    width: 900px;
    height: 514px;
    background: var(--card);
    box-shadow: 0 10px 30px var(--shadow);
    overflow: hidden;
  }

  /* Front */
  .contact-block {
    position: absolute;
    left: 70px;
    top: 150px;
    color: var(--navy);
  }
  .person-name {
    font-size: 40px;
    font-weight: 900;
    color: var(--brand-blue);
    letter-spacing: -0.5px;
  }
  .person-title {
    font-size: 21px;
    font-weight: 400;
    margin: 4px 0 26px 24px;
  }
  .contact-list { list-style: none; margin-left: 24px; }
  .contact-item {
    display: flex;
    align-items: flex-start;
    gap: 12px;
    font-size: 20px;
    line-height: 26px;
    margin-bottom: 4px;
  }
  .contact-icon { width: 20px; height: 20px; margin-top: 3px; flex: none; }
  .contact-values { display: flex; flex-direction: column; }

  .front-brand {
    position: absolute;
    right: 60px;
    top: 70px;
    display: flex;
    align-items: center;
    gap: 14px;
  }
  .brand-square {
    width: 34px;
    height: 34px;
    background: var(--brand-blue);
  }
  .brand-name {
    font-weight: 900;
    color: var(--brand-blue);
    text-transform: uppercase;
    letter-spacing: 2px;
  }
  .front-brand .brand-name { font-size: 38px; }

  .address-band {
    position: absolute;
    left: 0;
    right: 0;
    top: 372px;
    height: 66px;
    background: var(--brand-blue);
    color: var(--band-text);
    display: flex;
    align-items: center;
    justify-content: center;
    font-size: 22px;
    letter-spacing: 1px;
  }

  /* Back */
  .back-brand {
    position: absolute;
    inset: 0;
    display: flex;
    align-items: center;
    justify-content: center;
    gap: 26px;
  }
  .back-brand .brand-square { width: 64px; height: 64px; }
  .back-brand .brand-name { font-size: 66px; letter-spacing: 4px; }
</style>
</head>
<body>

<section class="card card-front">
  <div class="contact-block">
    <h1 class="person-name">Marco T. Bellini</h1>
    <p class="person-title">Manager</p>
    <ul class="contact-list">
      <li class="contact-item">
        <svg class="contact-icon" viewBox="0 0 20 20" aria-hidden="true">
          <circle cx="10" cy="10" r="10" fill="var(--navy)"/>
          <rect x="6.5" y="4.5" width="7" height="11" rx="1.2" fill="none" stroke="#fff" stroke-width="1.5"/>
          <circle cx="10" cy="13" r="0.9" fill="#fff"/>
        </svg>
        <span class="contact-values"><span>+212-555-0148</span><span>+212-555-0193</span></span>
      </li>
      <li class="contact-item">
        <svg class="contact-icon" viewBox="0 0 20 20" aria-hidden="true">
          <circle cx="10" cy="10" r="10" fill="var(--navy)"/>
          <rect x="5" y="6.5" width="10" height="7" fill="none" stroke="#fff" stroke-width="1.4"/>
          <path d="M5 6.5 L10 10.5 L15 6.5" fill="none" stroke="#fff" stroke-width="1.4"/>
        </svg>
        <span>marco@haldenworks.com</span>
      </li>
      <li class="contact-item">
        <svg class="contact-icon" viewBox="0 0 20 20" aria-hidden="true">
          <circle cx="10" cy="10" r="10" fill="var(--navy)"/>
          <circle cx="10" cy="10" r="5" fill="none" stroke="#fff" stroke-width="1.3"/>
          <ellipse cx="10" cy="10" rx="2.2" ry="5" fill="none" stroke="#fff" stroke-width="1.1"/>
          <line x1="5" y1="10" x2="15" y2="10" stroke="#fff" stroke-width="1.1"/>
        </svg>
        <span>www.haldenworks.com</span>
      </li>
    </ul>
  </div>

  <div class="front-brand">
    <span class="brand-square"></span>
    <span class="brand-name">Halden Works, Inc.</span>
  </div>

  <div class="address-band">118 Harbor Line Road - Brooklyn, New York 11231</div>
</section>

<section class="card card-back">
  <div class="back-brand">
    <span class="brand-square"></span>
    <span class="brand-name">Halden Works, Inc.</span>
  </div>
</section>

</body>
</html>
```